Business Card Design for The Lending Nook Inc.

We need a business card design for our mortgage company: "The Lending Nook Inc."

Need to have Social Media Account on there as a possibility

Industry/Entity Type

Business

```html
<!DOCTYPE html>
<html lang="en">
<head>
<meta charset="utf-8">
<title>The Lending Nook Inc. – Business Cards</title>
<link rel="stylesheet" href="https://fonts.googleapis.com/css2?family=Arimo:wght@400;700&display=swap">
<style>
  :root {
    --backdrop: #e8e9ec;
    --card: #fbfbfc;
    --brand-blue: #3b63a6;
    --navy: #1f3c8c;
    --ink: #2f3033;
    --rule: #3a3a3d;
  }
  * { box-sizing: border-box; margin: 0; padding: 0; }
  html, body {
    width: 1200px; height: 799px; overflow: hidden;
    background: var(--backdrop);
    font-family: "Arimo", Arial, sans-serif;
  }
  .stage { position: relative; width: 1200px; height: 799px; }
  .card {
    position: absolute; width: 530px; height: 303px;
    background: var(--card);
    box-shadow: 0 6px 18px rgba(0,0,0,0.12);
  }
  /* Front */
  .card-front { left: 50px; top: 110px; }
  .front-brand {
    position: absolute; left: 60px; top: 120px;
    display: flex; align-items: center; gap: 18px;
  }
  .brand-dot {
    width: 54px; height: 54px; border-radius: 50%;
    border: 3px solid var(--brand-blue);
  }
  .brand-name {
    color: var(--brand-blue); font-size: 38px; font-weight: 400;
    letter-spacing: -0.5px; white-space: nowrap;
  }
  .front-rule {
    position: absolute; left: 134px; top: 184px;
    width: 150px; height: 1.5px; background: var(--rule);
  }
  /* Back */
  .card-back { left: 620px; top: 386px; }
  .back-brand {
    position: absolute; left: 28px; top: 0; height: 303px; width: 220px;
    display: flex; flex-direction: column; align-items: center; justify-content: center; gap: 14px;
  }
  .back-brand .brand-dot { width: 70px; height: 70px; border-color: var(--navy); }
  .back-brand .brand-name { color: var(--navy); font-size: 20px; text-align: center; white-space: normal; }
  .divider {
    position: absolute; left: 262px; top: 40px;
    width: 1.5px; height: 223px; background: var(--rule);
  }
  .contact { position: absolute; left: 290px; top: 44px; }
  .person-name { color: var(--ink); font-size: 30px; line-height: 1.05; }
  .person-title { color: var(--navy); font-size: 15px; margin-top: 2px; }
  .contact-list { list-style: none; margin-top: 22px; font-size: 14px; color: var(--ink); line-height: 1.75; }
  .contact-list .label { color: var(--navy); }
  .social { display: flex; align-items: center; gap: 10px; margin-top: 22px; font-size: 14px; color: var(--ink); }
  .social-square { width: 22px; height: 22px; background: var(--navy); }
</style>
</head>
<body>
<main class="stage">
  <section class="card card-front" aria-label="Business card front">
    <div class="front-brand">
      <span class="brand-dot"></span>
      <span class="brand-name">The Lending Nook Inc.</span>
    </div>
    <div class="front-rule"></div>
  </section>

  <section class="card card-back" aria-label="Business card back">
    <div class="back-brand">
      <span class="brand-dot"></span>
      <span class="brand-name">The Lending Nook Inc.</span>
    </div>
    <div class="divider"></div>
    <div class="contact">
      <h1 class="person-name">Daniel Reyes</h1>
      <p class="person-title">Mortgage Advisor</p>
      <ul class="contact-list">
        <li><span class="label">t:</span> 555 (210) 4836</li>
        <li><span class="label">e:</span> hello@lendingnook.com</li>
        <li><span class="label">w:</span> www.lendingnook.com</li>
      </ul>
      <div class="social">
        <span class="social-square"></span>
        <span>The Lending Nook</span>
      </div>
    </div>
  </section>
</main>
</body>
</html>
```